Website to design and sell sundials: www.brelvaquest.com

We have a website that creates a free paper sundial, we want to migrate from this not profit free website to a website where we will continue offering the free paper sundial model but We will also offer a manufactured sundial and sell it.
In order to understand the project, please visit:
http://www.brelvaquest.com/vertical/sundial.html and
http://www.korutel.net/landing/

The website user journey should be redesigned, including the phases that are,
select language
Show product give info
Creation/edit sundial (could be one or more phases)
View created sundial
Buy sundial.

May some of them could be combined or splitted, what It have more sense.

Coded - Design and coding required

4 page

Sans Serif

• A description page user journey offering freemium paper sundial and physical sundial to sell.
• A sundial creation page for "free" paper sundial
• A result page for paper sundial
• A sell page for physical

```html
<!DOCTYPE html>
<html lang="en">
<head>
<meta charset="utf-8">
<title>BrelvaQuest – Sundials</title>
<link rel="stylesheet" href="https://fonts.googleapis.com/css2?family=Raleway:wght@400;500;600;700;800&display=swap">
<style>
:root{
  --red:#b30a06;
  --red-dark:#8f0603;
  --black:#111;
  --ink:#222;
  --white:#fff;
  --page:#dcdcdc;
  --pink:#f7dede;
  --form-field:#e4e4e4;
  --footer:#e9e9e9;
  --muted:#777;
}
*{box-sizing:border-box;margin:0;padding:0}
html,body{width:1200px;height:2899px;overflow:hidden}
body{position:relative;background:var(--page);font-family:"Raleway",sans-serif;color:var(--ink)}
.abs{position:absolute}

/* header */
.site-header{left:0;top:0;width:1200px;height:113px;background:var(--white)}
.brand{left:90px;top:34px;display:flex;align-items:center;gap:12px}
.brand-mark{width:30px;height:30px;border-radius:50%;background:var(--red)}
.brand-name{font-size:30px;font-weight:700;color:var(--red)}
.lang{left:1050px;top:18px;font-size:14px;display:flex;align-items:center;gap:8px}
.lang-dot{width:20px;height:20px;border-radius:50%;background:var(--red);border:3px solid var(--white);box-shadow:0 0 0 1px #ccc}
.step-btn{top:55px;height:42px;width:106px;background:var(--red);color:var(--white);border-radius:5px;font-size:11px;font-weight:600;display:flex;align-items:center;justify-content:center;text-align:center;line-height:1.1;box-shadow:0 2px 3px rgba(0,0,0,.3)}

/* nav */
.main-nav{left:0;top:113px;width:1200px;height:103px;background:var(--red)}
.nav-item{top:0;height:103px;display:flex;align-items:center;color:var(--white);font-size:20px;font-weight:700;text-transform:uppercase}
.nav-item.active{left:90px;width:142px;background:var(--black);justify-content:center;text-transform:none}

/* hero */
.hero-photo{left:0;top:216px;width:1200px;height:530px;background:linear-gradient(180deg,#5d6168 0%,#8e9096 45%,#7a6a55 65%,#4f4636 100%)}
.register{left:87px;top:251px;width:353px;height:409px;background:var(--red)}
.register-head{height:39px;background:#1f2a28;color:var(--white);font-size:20px;font-weight:500;display:flex;align-items:center;justify-content:center}
.field-label{left:44px;color:var(--white);font-size:16px;font-weight:700}
.field{left:233px;width:180px;height:32px;background:var(--form-field);border-radius:4px}

/* intro */
.intro-head{left:87px;top:669px;width:1023px;height:71px;background:var(--pink);display:flex;justify-content:center;padding-top:14px}
.intro-head h2{font-size:32px;font-weight:700;color:var(--black);border-bottom:3px solid var(--red);height:44px}
.intro-body{left:87px;top:740px;width:1023px;height:386px;background:var(--red)}
.intro-thumb{width:113px;height:113px;border-radius:50%;background:radial-gradient(circle,#fafafa 40%,#cfcfcf 100%)}
.intro-text{width:540px;color:var(--white);font-size:16px;font-weight:600;line-height:1.35}
.read-more{display:inline-block;background:var(--black);color:var(--white);font-size:12px;padding:3px 10px;border-radius:3px;margin-left:10px}

/* product */
.product-frame{left:129px;top:1255px;width:408px;height:263px;border:5px solid var(--red);padding:10px}
.product-photo{width:100%;height:100%;background:linear-gradient(135deg,#3f5a2b,#6f8d4a 50%,#3a4f26)}
.product-specs{left:611px;top:1262px;font-size:17px;line-height:1.5;color:var(--ink)}
.product-specs small{display:block;font-size:13px;line-height:1.5}
.order-btn{left:476px;top:1554px;width:296px;height:80px;background:var(--black);border:4px solid #888;border-radius:8px;color:var(--white);font-size:38px;font-weight:600;display:flex;align-items:center;justify-content:center;gap:10px}

/* needs */
.needs{left:0;top:1673px;width:1200px;height:476px;background:var(--red);clip-path:polygon(0 0,100% 64px,100% 100%,0 420px)}
.needs-icon{left:555px;top:1730px;width:48px;height:48px;border-radius:50%;background:var(--black);color:var(--white);font-size:32px;font-weight:800;display:flex;align-items:center;justify-content:center}
.needs-title{left:0;width:1200px;top:1790px;text-align:center;font-size:32px;font-weight:800;color:var(--black)}
.needs-title span{border-bottom:3px solid var(--white)}
.needs-col{top:1866px;color:var(--white);font-size:15px;font-weight:600;line-height:1.4}
.needs-col h3{font-size:20px;font-weight:600;color:var(--black);margin-bottom:8px}

/* instructions */
.instr{left:87px;top:2290px;width:1023px;height:316px;background:var(--red)}
.instr-icon{left:262px;top:2300px}
.instr-diagram{left:177px;top:2400px;width:306px;height:190px;background:var(--white);border:1px solid #999}
.instr-panel{left:595px;top:2290px;width:515px;height:316px;background:var(--black);color:var(--white);padding:18px 30px}
.instr-panel h3{text-align:center;font-size:24px;font-weight:700;margin-bottom:14px}
.instr-panel ol{list-style:none;font-size:13px;line-height:1.55}
.custom-btn{left:733px;top:2548px;width:232px;height:34px;background:var(--red);color:var(--white);font-size:15px;font-weight:600;border-radius:3px;display:flex;align-items:center;justify-content:center}

/* footer */
.contact-strip{left:0;top:2709px;width:1200px;height:122px;background:var(--footer)}
.contact-item{top:2709px;height:122px;display:flex;align-items:center;gap:14px;color:#666}
.contact-item b{font-size:32px;font-weight:500;display:block;line-height:1}
.contact-item small{font-size:13px}
.divider{top:2725px;width:2px;height:90px;background:#ccc}
.social{display:flex;gap:6px;margin-top:4px}
.social i{width:18px;height:18px;border-radius:50%;border:2px solid #777;display:block}
.bottom-bar{left:0;top:2831px;width:1200px;height:68px;background:var(--white);font-size:14px;color:var(--muted)}
.bottom-bar p{position:absolute;top:24px}
</style>
</head>
<body>

<header class="site-header abs">
  <div class="brand abs"><span class="brand-mark"></span><span class="brand-name">BrelvaQuest</span></div>
  <div class="lang abs">Language <span class="lang-dot"></span></div>
  <div class="step-btn abs" style="left:537px">Show product</div>
  <div class="step-btn abs" style="left:708px">Creation And modify</div>
  <div class="step-btn abs" style="left:862px">View sundial</div>
  <div class="step-btn abs" style="left:1023px">Buy sundial</div>
</header>

<nav class="main-nav abs">
  <div class="nav-item active abs">Home</div>
  <div class="nav-item abs" style="left:280px">About us</div>
  <div class="nav-item abs" style="left:472px">Work</div>
  <div class="nav-item abs" style="left:625px">Link</div>
  <div class="nav-item abs" style="left:762px">Contact us</div>
  <div class="nav-item abs" style="left:968px">Clients</div>
</nav>

<div class="hero-photo abs" role="img" aria-label="Large metal sundial sculpture in a field under a cloudy sky"></div>

<form class="register abs">
  <div class="register-head">Register now</div>
  <span class="field-label abs" style="top:82px">Name :</span><span class="field abs" style="top:76px"></span>
  <span class="field-label abs" style="top:138px">Email ID :</span><span class="field abs" style="top:132px"></span>
  <span class="field-label abs" style="top:194px">Phone no :</span><span class="field abs" style="top:188px"></span>
  <span class="field-label abs" style="top:244px">Message :</span><span class="field abs" style="top:240px;height:96px"></span>
</form>

<section>
  <div class="intro-head abs"><h2>Introduction</h2></div>
  <div class="intro-body abs">
    <div class="intro-thumb abs" role="img" aria-label="Paper sundial with hour lines" style="left:138px;top:64px"></div>
    <p class="intro-text abs" style="left:325px;top:70px">This page is about Sundials. Sundials are instruments that tell you the time with the shadow of the sun. To design a sundial you need to know exactly where you are going to put it, .............. <span class="read-more">Read more</span></p>
    <div class="intro-thumb abs" role="img" aria-label="Wall mounted sundial plate" style="left:138px;top:225px"></div>
    <p class="intro-text abs" style="left:325px;top:225px">This page is about Sundials. Sundials are instruments that tell you the time with the shadow of the sun. To design a sundial you need to know exactly where you are going to put it, .............. <span class="read-more">Read more</span></p>
  </div>
</section>

<section>
  <div class="product-frame abs"><div class="product-photo" role="img" aria-label="Steel sundial plate lying on grass"></div></div>
  <div class="product-specs abs">
    Size 245mm x 345 mm<br>Methacrylate board 3mm thick with rounded corners.<br>Steel like cover.
    <small>Customized laser engraved with hour lines<br>Customized Gnomon 3mm thick with fittings for board holes<br>Shipping to EU</small>
  </div>
  <div class="order-btn abs">ORDER NOW
    <svg width="34" height="30" viewBox="0 0 34 30"><path d="M1 3h6l4 16h17l4-12H9" fill="none" stroke="#fff" stroke-width="3"/><circle cx="13" cy="26" r="3" fill="#fff"/><circle cx="26" cy="26" r="3" fill="#fff"/></svg>
  </div>
</section>

<section>
  <div class="needs abs"></div>
  <div class="needs-icon abs">?</div>
  <h2 class="needs-title abs"><span>WHAT YOU NEED</span></h2>
  <div class="needs-col abs" style="left:193px">
    <h3>You need to have</h3>
    1. This webpage<br>2. A printer<br>3. Scissors
  </div>
  <div class="needs-col abs" style="left:508px;width:330px">
    <h3>You need to know</h3>
    1. Where is the wall where you want to put your sundial on, located it with Terravista Maps<br>-Click once at one end of a long wall.<br>-Move to and click again on the other end.<br>This draws a red line parallel to the wall, and defines the orientation<br>Zoom in as far as possible.
  </div>
  <div class="needs-col abs" style="left:878px;top:1890px;width:260px">
    2. Select the N/S/E/W face desired, from the pull-down menu<br>3. Select your timezone or true local time for solar time<br>4. Select if you are daylight saving time
  </div>
</section>

<section>
  <div class="instr abs"></div>
  <svg class="instr-icon abs" width="90" height="80" viewBox="0 0 110 90" role="img" aria-label="Hand holding a sundial icon">
    <circle cx="55" cy="24" r="18" fill="#111"/>
    <rect x="20" y="52" width="70" height="10" rx="5" fill="#111"/>
    <path d="M20 62 q35 25 70 0" fill="none" stroke="#fff" stroke-width="6"/>
  </svg>
  <div class="instr-diagram abs" role="img" aria-label="Diagram of a vertical sundial layout with hour lines"></div>
  <div class="instr-panel abs">
    <h3>INSTRUCTIONS</h3>
    <ol>
      <li>1. CALCULATE</li>
      <li>2. PRINT THE PDF: to print, please select 'shrink to page' in order not to deform the shape of the page.</li>
      <li>3. CUT AND FOLD: Once you have your model printed, you have to cut RED LINES, and FOLD BLUE LINES</li>
      <li>4. PUT ON YOUR WALL the dial on your wall or window</li>
      <li>5. ENJOY.</li>
    </ol>
  </div>
  <div class="custom-btn abs">Custom sundial</div>
</section>

<footer>
  <div class="contact-strip abs"></div>
  <div class="contact-item abs" style="left:95px">
    <svg width="44" height="44" viewBox="0 0 24 24"><path d="M6 2l3 4-2 2c1 3 4 6 7 7l2-2 4 3-2 4C10 20 4 14 2 6z" fill="#888"/></svg>
    <div><b>Contact us</b><small>(555) 014-2276</small></div>
  </div>
  <div class="divider abs" style="left:318px"></div>
  <div class="contact-item abs" style="left:350px">
    <svg width="50" height="50" viewBox="0 0 24 24"><path d="M10 14l4-4M8 11l-3 3a3 3 0 0 0 5 5l3-3M16 13l3-3a3 3 0 0 0-5-5l-3 3" fill="none" stroke="#aaa" stroke-width="2"/></svg>
    <div><b>Link</b></div>
  </div>
  <div class="divider abs" style="left:585px"></div>
  <div class="contact-item abs" style="left:615px">
    <svg width="44" height="44" viewBox="0 0 24 24"><path d="M2 10h4v11H2zM8 21V10l5-8c2 0 2 2 2 4l-1 4h6c1 0 2 1 2 2l-2 8c0 1-1 1-2 1z" fill="#888"/></svg>
    <div><b>Connect Us</b><span class="social"><i></i><i></i><i></i><i></i></span></div>
  </div>
  <div class="divider abs" style="left:870px"></div>
  <div class="contact-item abs" style="left:900px">
    <svg width="46" height="44" viewBox="0 0 24 24"><path d="M3 4h18v12H9l-5 4v-4H3z" fill="none" stroke="#888" stroke-width="2"/></svg>
    <div><b>Chat with us</b><small>Real time chat with our team</small></div>
  </div>
  <div class="bottom-bar abs">
    <p style="left:20px">© 2014 Tavimoor. All rights reserved.</p>
    <p style="left:785px">Privacy Policy | Terms of Use | Copyright | Site Map</p>
  </div>
</footer>

</body>
</html>
```